Logistics and freight company requires website

Hi, a logistic and freight company which is based in the United States needs an industry standard website for its activities. We are into forwarding and courier goods from within United States and Canada. We deliver a wide range of goods from shipping of electronics to document, clothings, etc. The proposed website should be comtemporary and youthful. I require brilliant colors for the website. The website should be the basic things of a site. There should a category for shipping electronics, clothings, documents and others( stuffs not listed within the three I mentioned).

```html
<!DOCTYPE html>
<html lang="en">
<head>
<meta charset="utf-8">
<title>Northway Freight</title>
<link href="https://fonts.googleapis.com/css2?family=PT+Sans:wght@400;700&display=swap" rel="stylesheet">
<style>
:root{
  --blue:#0d4f9e;
  --teal:#1aa3c9;
  --footer:#1f9fc5;
  --footer-dark:#1a8cb0;
  --gray:#efefef;
  --text:#555;
  --dark:#222;
  --line:#d8d8d8;
  --white:#fff;
  --client:#a9a9a9;
}
*{margin:0;padding:0;box-sizing:border-box}
html,body{width:1200px;height:2466px;overflow:hidden}
body{position:relative;background:var(--white);font-family:"PT Sans",sans-serif;color:var(--text)}
.abs{position:absolute}
a{color:inherit;text-decoration:none}

/* header */
.header{left:0;top:0;width:1200px;height:125px;background:var(--white)}
.brand{left:74px;top:44px;font-size:34px;color:var(--dark);letter-spacing:.5px}
.top-contact{right:74px;top:26px;font-size:16px;color:var(--blue);display:flex;align-items:center;gap:10px}
.top-contact svg{width:16px;height:16px;fill:var(--blue)}
.top-contact .sep{margin:0 4px}
.nav{right:74px;top:80px;display:flex;gap:34px;font-size:13px;font-weight:700;color:var(--dark);letter-spacing:.3px}
.nav a{padding-bottom:8px}
.nav a.active{color:var(--teal);border-bottom:2px solid var(--teal);padding:0 10px 8px}

/* hero */
.hero{left:0;top:125px;width:1200px;height:458px;background:linear-gradient(120deg,#0a3f8a 0%,#1f6fd0 45%,#3b8be6 70%,#0e4fa5 100%)}
.hero-line{left:74px;background:rgba(255,255,255,.88);color:var(--dark);font-size:35px;font-weight:700;padding:2px 12px}
.hero-dots{left:74px;top:536px;display:flex;gap:8px}
.hero-dots span{width:11px;height:11px;border-radius:50%;background:var(--white)}
.hero-dots span:first-child{background:#7fb1e6}

/* headings */
.h2{font-size:28px;font-weight:400;color:var(--dark);text-transform:uppercase}
.h2 b{color:var(--blue);font-weight:700}
.btn{display:inline-block;background:var(--teal);color:var(--white);font-size:12.5px;font-weight:700;text-transform:uppercase;text-align:center;line-height:41px;height:41px}
p{font-size:13.5px;line-height:24px}

/* welcome */
.welcome-title{left:74px;top:624px}
.welcome-text{left:74px;top:668px;width:665px}
.welcome-btn{left:74px;top:823px;width:138px}
.welcome-img{left:750px;top:625px;width:380px;height:250px;border-radius:6px;background:radial-gradient(ellipse at center,#dfe6ef 0%,#f4f6f9 60%,#fff 100%)}

/* services */
.services{left:0;top:891px;width:1200px;height:399px;background:var(--gray)}
.services-title{left:74px;top:1056px;line-height:32px}
.services-divider{left:316px;top:993px;width:2px;height:197px;background:#c8c8c8}
.svc-icon{width:84px;height:84px;border-radius:50%;background:var(--blue);display:flex;align-items:center;justify-content:center}
.svc-icon svg{width:44px;height:44px;fill:none;stroke:var(--white);stroke-width:3;stroke-linejoin:round}
.svc-title{font-size:15px;font-weight:700;color:var(--blue);text-transform:uppercase}
.svc-text{width:230px;font-size:13px;line-height:21px}

/* why */
.thumb{width:242px;height:175px}
.why-title{left:342px;font-size:26px}
.why-text{left:342px;width:410px}
.why-btn{left:342px;width:138px}
.why-divider{left:74px;top:1545px;width:678px;height:1px;background:var(--line)}
.col-divider{left:780px;top:1333px;width:1px;height:427px;background:var(--line)}

/* news */
.news-title{left:810px;top:1326px;font-size:27px}
.news-item{left:810px;width:316px;height:106px;border-bottom:1px solid var(--line)}
.date{position:absolute;left:0;top:0;width:54px;height:74px;border-radius:4px;overflow:hidden;text-align:center}
.date .m{background:var(--teal);color:var(--white);font-size:13px;height:24px;line-height:24px}
.date .d{background:#222;color:var(--white);font-size:30px;font-weight:700;height:50px;line-height:50px}
.news-body{position:absolute;left:78px;top:0;width:238px}
.news-head{font-size:13.5px;font-weight:700;color:var(--blue);line-height:21px}
.news-sum{font-size:13px;line-height:21px}
.news-more{font-size:13px;color:var(--teal);font-weight:700}
.news-all{right:76px;top:1734px;font-size:13.5px;font-weight:700;color:var(--blue)}

/* cta */
.cta{left:0;top:1790px;width:1200px;height:246px;background:linear-gradient(90deg,#3d4a5c 0%,#56657a 45%,#3a4659 70%,#27303f 100%)}
.cta-text{left:0;top:1852px;width:1200px;text-align:center;color:var(--white);font-size:26px;line-height:36px;text-transform:uppercase}
.cta-text b{font-weight:700}
.cta-btn{left:532px;top:1944px;width:138px}

/* clients */
.clients-title{left:0;top:2076px;width:1200px;text-align:center}
.clients-row{left:74px;top:2140px;width:1052px;display:flex;justify-content:space-between;align-items:center;height:60px}
.client{font-size:30px;font-weight:700;color:var(--client);display:flex;align-items:center;gap:10px}
.client i{display:block;width:14px;height:14px;border-radius:50%;background:var(--client)}

/* footer */
.footer{left:0;top:2230px;width:1200px;height:236px;background:var(--footer)}
.f-col{top:2270px;color:var(--white);font-size:13px;line-height:28px}
.f-col h4{font-size:13.5px;font-weight:700;text-transform:uppercase;margin-bottom:6px;line-height:20px}
.f-sep{top:2250px;width:1px;height:196px;background:var(--footer-dark)}
.socials{display:flex;gap:10px;margin-top:8px}
.socials span{width:30px;height:30px;border-radius:50%;background:#1c4f8a}
.socials span:nth-child(2){background:#2a8fd6}
.socials span:nth-child(3){background:#4a4a4a}
.socials span:nth-child(4){background:#1f6ea8}
.socials span:nth-child(5){background:#f08a1c}
.copy{font-size:12px;line-height:20px;margin-top:18px}
</style>
</head>
<body>

<header class="header abs">
  <div class="brand abs">NORTHWAY FREIGHT</div>
  <div class="top-contact abs">
    <svg viewBox="0 0 24 24"><path d="M6.6 10.8a15 15 0 0 0 6.6 6.6l2.2-2.2a1 1 0 0 1 1-.25 11.4 11.4 0 0 0 3.6.57 1 1 0 0 1 1 1V20a1 1 0 0 1-1 1A17 17 0 0 1 3 4a1 1 0 0 1 1-1h3.5a1 1 0 0 1 1 1c0 1.25.2 2.45.57 3.6a1 1 0 0 1-.25 1z"/></svg>
    <b>1-800-555-0142</b><span class="sep">|</span>
    <svg viewBox="0 0 24 24"><path d="M2 5h20v14H2z M2 5l10 8 10-8" /></svg>
    <span>info@northwayfreight.com</span>
  </div>
  <nav class="nav abs">
    <a class="active">HOME</a><a>ABOUT US</a><a>SERVICES</a><a>LATEST NEWS</a><a>BLOG</a><a>CLIENTS</a><a>CONTACT US</a>
  </nav>
</header>

<section class="hero abs" role="img" aria-label="Cargo ship, container crane, jet and globe over a world map in blue tones"></section>
<div class="hero-line abs" style="top:302px">We are a Logistic &amp; Freight Service</div>
<div class="hero-line abs" style="top:355px">Based in the United States</div>
<div class="hero-dots abs"><span></span><span></span><span></span><span></span></div>

<h2 class="h2 welcome-title abs">Welcome to <b>Northway Freight</b></h2>
<p class="welcome-text abs">Aliquam molestie, mi et imperdiet euismod, dui purus auctor tellus, et interdum lacus lectus et ante. Sed accumsan sollicitudin sapien, sit amet adipiscing turpis gravida ac. In congue, neque ac lobortis volutpat, libero mauris varius mi, vitae suscipit ipsum ligula vitae risus. Duis aliquam nibh a dui iaculis viverra id a velit. Vivamus egestas risus in magna varius commodo. Sed semper viverra egestas. Etiam pretium porttitor lectus, vel ornare neque porta volutpat.</p>
<a class="btn welcome-btn abs">Read More</a>
<div class="welcome-img abs" role="img" aria-label="Cargo plane, trucks, container ship and delivery van grouped together"></div>

<section class="services abs"></section>
<h2 class="h2 services-title abs">Our <b>Services<br>Offers</b></h2>
<div class="services-divider abs"></div>

<div class="svc-icon abs" style="left:378px;top:974px"><svg viewBox="0 0 44 44"><rect x="4" y="12" width="24" height="18"/><path d="M28 18h8l5 6v6H28z"/><circle cx="12" cy="32" r="3.5"/><circle cx="34" cy="32" r="3.5"/></svg></div>
<div class="svc-title abs" style="left:487px;top:972px">Logistic</div>
<p class="svc-text abs" style="left:487px;top:994px">Aliquam molestie, mi et imperdiet euismod, dui purus auctor tellus, et interdum lacus lectus et ante.</p>

<div class="svc-icon abs" style="left:779px;top:974px"><svg viewBox="0 0 44 44"><path d="M5 26h34l-5 9H10z"/><rect x="12" y="14" width="8" height="12"/><rect x="22" y="10" width="8" height="16"/></svg></div>
<div class="svc-title abs" style="left:888px;top:972px">Freight</div>
<p class="svc-text abs" style="left:888px;top:994px">Aliquam molestie, mi et imperdiet euismod, dui purus auctor tellus, et interdum lacus lectus et ante.</p>

<div class="svc-icon abs" style="left:378px;top:1117px"><svg viewBox="0 0 44 44"><rect x="8" y="14" width="28" height="22"/><path d="M8 14l6-6h16l6 6M22 14v8"/></svg></div>
<div class="svc-title abs" style="left:487px;top:1115px">Shipping of Electronics</div>
<p class="svc-text abs" style="left:487px;top:1137px">Aliquam molestie, mi et imperdiet euismod, dui purus auctor tellus, et interdum lacus lectus et ante.</p>

<div class="svc-icon abs" style="left:779px;top:1117px"><svg viewBox="0 0 44 44"><path d="M10 6h18l6 6v26H10z"/><path d="M15 16h14M15 22h14M15 28h10"/></svg></div>
<div class="svc-title abs" style="left:888px;top:1115px">Document</div>
<p class="svc-text abs" style="left:888px;top:1137px">Aliquam molestie, mi et imperdiet euismod, dui purus auctor tellus, et interdum lacus lectus et ante.</p>

<div class="thumb abs" style="left:74px;top:1333px;background:linear-gradient(160deg,#3a6fb8,#c79a5c 60%,#8a6a3e)" role="img" aria-label="Cardboard parcels on a laptop keyboard"></div>
<h2 class="h2 why-title abs" style="top:1326px">Why <b>Northway Freight?</b></h2>
<p class="why-text abs" style="top:1368px">Aliquam molestie, mi et imperdiet euismod, dui purus auctor tellus, et interdum lacus lectus et ante. Sed accumsan sollicitudin sapien, sit amet adipiscing turpis gravida ac.</p>
<a class="btn why-btn abs" style="top:1468px">Read More</a>
<div class="why-divider abs"></div>

<div class="thumb abs" style="left:74px;top:1581px;background:linear-gradient(160deg,#6a4a36,#b08a62 55%,#d6b48a)" role="img" aria-label="Warehouse worker packing parcels"></div>
<h2 class="h2 why-title abs" style="top:1574px">Wide <b>Range of Shipping</b></h2>
<p class="why-text abs" style="top:1616px">Aliquam molestie, mi et imperdiet euismod, dui purus auctor tellus, et interdum lacus lectus et ante. Sed accumsan sollicitudin sapien, sit amet adipiscing turpis gravida ac.</p>
<a class="btn why-btn abs" style="top:1714px">Read More</a>

<div class="col-divider abs"></div>

<h2 class="h2 news-title abs">Latest <b>News</b></h2>
<div class="news-item abs" style="top:1374px">
  <div class="date"><div class="m">FEB</div><div class="d">10</div></div>
  <div class="news-body"><div class="news-head">Aliquam molestie mi et imperdiet euismod...</div><div class="news-sum">Sed accumsan sollicitudin sapien...</div><div class="news-more">Read More</div></div>
</div>
<div class="news-item abs" style="top:1491px">
  <div class="date"><div class="m">FEB</div><div class="d">10</div></div>
  <div class="news-body"><div class="news-head">Aliquam molestie mi et imperdiet euismod...</div><div class="news-sum">Sed accumsan sollicitudin sapien...</div><div class="news-more">Read More</div></div>
</div>
<div class="news-item abs" style="top:1610px;border-bottom:none">
  <div class="date"><div class="m">FEB</div><div class="d">10</div></div>
  <div class="news-body"><div class="news-head">Aliquam molestie mi et imperdiet euismod...</div><div class="news-sum">Sed accumsan sollicitudin sapien...</div><div class="news-more">Read More</div></div>
</div>
<a class="news-all abs">READ ALL NEWS &raquo;</a>

<section class="cta abs" role="img" aria-label="Port cranes and a businessman using a tablet in grey-blue tones"></section>
<div class="cta-text abs">Forwarding and courier goods from within<br><b>United States and Canada</b></div>
<a class="btn cta-btn abs">Contact Us</a>

<h2 class="h2 clients-title abs">Our <b>Clients</b></h2>
<div class="clients-row abs">
  <div class="client">QUORVANE</div>
  <div class="client"><i></i>Brellix</div>
  <div class="client">Ostamere Partners</div>
  <div class="client">VANTORLY</div>
  <div class="client">DRAVIK</div>
</div>

<footer class="footer abs"></footer>
<div class="f-col abs" style="left:74px"><h4>Company</h4>Home<br>About Us<br>Services<br>Latest News</div>
<div class="f-col abs" style="left:207px;top:2296px">Blog<br>Clients<br>Contact us</div>
<div class="f-sep abs" style="left:316px"></div>
<div class="f-col abs" style="left:347px"><h4>Services</h4>Aliquam molestie<br>Vestibulum ante ipsum<br>Fusce accumsan<br>Suspendisse lobortis</div>
<div class="f-sep abs" style="left:535px"></div>
<div class="f-col abs" style="left:573px;line-height:21px"><h4 style="margin-bottom:10px">Contact Us</h4><b style="font-size:14px">Northway Freight</b><br>1420 Harlow Avenue,<br>Dayton, OH 45402<br><div style="margin-top:12px"><b>Ph: 1-800-555-0142</b><br><b>Email: info@northwayfreight.com</b></div></div>
<div class="f-sep abs" style="left:850px"></div>
<div class="f-col abs" style="left:888px"><h4>Connect Us</h4>
  <div class="socials"><span></span><span></span><span></span><span></span><span></span></div>
  <div class="copy">Copyright &copy; 2016. Northway Freight<br>All Right Reserved</div>
</div>

</body>
</html>
```